PowerPoint template for my training workshop business

I would like to have a PowerPoint template created using my logo and palette materials created by Brindlework. I train and facilitate workshops using PowerPoint in both corporate and public settings.

I have attached the original design elements to this request.

```html
<!DOCTYPE html>
<html lang="en">
<head>
<meta charset="utf-8">
<title>Brindlework – Workshop Presentation Template</title>
<link href="https://fonts.googleapis.com/css2?family=Cinzel:wght@400&family=Open+Sans:wght@400;600;700&display=swap" rel="stylesheet">
<style>
:root{
  --orange:#f39a1e;
  --yellow:#f7b500;
  --magenta:#9b2a5e;
  --teal:#0f4a4e;
  --black:#141414;
  --grey:#c4c4c4;
  --ink:#555;
  --white:#fff;
  --ph-field:linear-gradient(180deg,#f7e9bd 0%,#d9b25c 45%,#6d6a2e 80%,#3c4422 100%);
  --ph-warm:linear-gradient(135deg,#f9d98a 0%,#e39a43 40%,#7a4a34 75%,#3a2a26 100%);
  --ph-sunset:linear-gradient(180deg,#4e3b7a 0%,#c4527f 45%,#f28a3e 75%,#2a1e24 100%);
  --ph-lake:linear-gradient(180deg,#e9c27a 0%,#b5874e 40%,#5a5a4e 70%,#2e3530 100%);
  --ph-interior:linear-gradient(135deg,#d7c9b8 0%,#8f7a6a 45%,#b8343e 75%,#3a2a2a 100%);
  --ph-meadow:linear-gradient(160deg,#fff1c4 0%,#f0c46a 30%,#8a6a9a 60%,#4f6a2e 100%);
  --ph-flowers:linear-gradient(160deg,#d9ddd0 0%,#a9b39a 40%,#d9b29a 70%,#6f7d5c 100%);
}
*{box-sizing:border-box;margin:0;padding:0}
html,body{width:813px;height:1200px;overflow:hidden;background:#fff}
body{font-family:"Open Sans",Arial,sans-serif;color:var(--ink)}
.canvas{position:relative;width:813px;height:1200px;overflow:hidden;background:#fff}
.slide{position:absolute;width:261px;height:148px;background:#fff;overflow:hidden;box-shadow:0 1px 4px rgba(0,0,0,.25)}
.slide>*{position:absolute}
.photo{display:block}
.swoosh{left:0;top:0;width:100%;height:100%}
.ttl{font-family:"Cinzel",Georgia,serif;color:var(--orange);letter-spacing:.3px;line-height:1;white-space:nowrap}
.ttl-w{color:#fff}
.logo{width:14px;height:14px;border-radius:50%;border:2.5px solid var(--orange);background:#fff}
.tiny{font-size:3.2px;line-height:1.35;color:#666}
.small{font-size:4.2px;line-height:1.35;color:#666}
.lbl{font-size:4px;color:#555;text-transform:uppercase;letter-spacing:.2px;white-space:nowrap}
.w{color:#fff}
.badge{width:14px;height:14px;border-radius:50%;background:var(--orange);color:#fff;font-family:"Cinzel",serif;font-size:8px;display:flex;align-items:center;justify-content:center;border:1.5px solid #fff}
.icon-c{width:16px;height:16px;border-radius:50%;background:var(--magenta);display:flex;align-items:center;justify-content:center}
.icon-c svg{width:10px;height:10px}
.bar{color:#fff;padding:2px 4px}
.bar b{display:block;font-size:3.4px;font-weight:600}
.bar span{display:block;font-size:3.4px}
.num{width:12px;height:12px;border-radius:50%;color:#fff;font-size:6px;display:flex;align-items:center;justify-content:center;font-family:"Cinzel",serif}
</style>
</head>
<body>
<svg width="0" height="0" style="position:absolute" aria-hidden="true">
  <symbol id="i-thumb" viewBox="0 0 24 24"><path fill="currentColor" d="M2 10h4v11H2zM8 10l5-8c2 0 3 1 2.5 3L14 9h6c1.5 0 2.5 1.2 2 2.6l-2.5 8C19 20.5 18.3 21 17.4 21H8z"/></symbol>
  <symbol id="i-target" viewBox="0 0 24 24"><g fill="none" stroke="currentColor" stroke-width="2"><circle cx="11" cy="13" r="9"/><circle cx="11" cy="13" r="5"/></g><circle cx="11" cy="13" r="1.8" fill="currentColor"/><path d="M11 13L21 3M17 3h4v4" stroke="currentColor" stroke-width="2" fill="none"/></symbol>
  <symbol id="i-puzzle" viewBox="0 0 24 24"><path fill="currentColor" d="M4 7h4a3 3 0 1 1 6 0h4v4a3 3 0 1 1 0 6v4h-4a3 3 0 1 0-6 0H4v-4a3 3 0 1 0 0-6z"/></symbol>
  <symbol id="i-bulb" viewBox="0 0 24 24"><path fill="none" stroke="currentColor" stroke-width="2" d="M12 2a7 7 0 0 0-4 12.7V18h8v-3.3A7 7 0 0 0 12 2zM9 21h6"/></symbol>
  <symbol id="i-hourglass" viewBox="0 0 24 24"><path fill="currentColor" d="M6 2h12v2c0 4-3 6-4.5 8C15 14 18 16 18 20v2H6v-2c0-4 3-6 4.5-8C9 10 6 8 6 4z"/></symbol>
  <symbol id="i-eye" viewBox="0 0 24 24"><path fill="none" stroke="currentColor" stroke-width="2" d="M1 12s4-7 11-7 11 7 11 7-4 7-11 7S1 12 1 12z"/><circle cx="12" cy="12" r="3.5" fill="currentColor"/></symbol>
  <symbol id="i-smile" viewBox="0 0 24 24"><g fill="none" stroke="currentColor" stroke-width="2"><circle cx="12" cy="12" r="10"/><path d="M7 14c2 3 8 3 10 0"/></g><circle cx="9" cy="9" r="1.3" fill="currentColor"/><circle cx="15" cy="9" r="1.3" fill="currentColor"/></symbol>
  <symbol id="i-award" viewBox="0 0 24 24"><g fill="none" stroke="currentColor" stroke-width="2.4"><circle cx="12" cy="9" r="6"/><path d="M8 14l-2 8 6-3 6 3-2-8"/></g></symbol>
  <symbol id="i-check" viewBox="0 0 24 24"><path fill="none" stroke="currentColor" stroke-width="3" d="M5 12l5 5 9-10"/></symbol>
  <symbol id="i-pin" viewBox="0 0 24 24"><path fill="currentColor" d="M12 2a7 7 0 0 0-7 7c0 5 7 13 7 13s7-8 7-13a7 7 0 0 0-7-7zm0 10a3 3 0 1 1 0-6 3 3 0 0 1 0 6z"/></symbol>
  <symbol id="i-heart" viewBox="0 0 24 24"><path fill="currentColor" d="M12 21S3 14 3 8.5A4.5 4.5 0 0 1 12 6a4.5 4.5 0 0 1 9 2.5C21 14 12 21 12 21z"/></symbol>
  <symbol id="i-dollar" viewBox="0 0 24 24"><path fill="none" stroke="currentColor" stroke-width="2.4" d="M16 7c-1-1.5-7-2-7 1.5S16 11 16 15s-6 3.5-8 1.5M12 3v18"/></symbol>
</svg>

<main class="canvas">

<!-- Row 1 -->
<section class="slide title-slide" style="left:5px;top:13px">
  <div class="photo" style="left:0;top:50px;width:261px;height:98px;background:var(--ph-field)" role="img" aria-label="Photo of a woman sitting in a sunlit meadow"></div>
  <svg class="swoosh" viewBox="0 0 262 148" preserveAspectRatio="none">
    <path d="M0 0H262V60Q160 96 0 80Z" fill="#fff"/>
    <path d="M0 80Q160 96 262 60V66Q150 100 0 84Z" fill="var(--grey)"/>
    <path d="M0 84Q150 100 262 66V74Q150 110 0 90Z" fill="var(--orange)"/>
  </svg>
  <div class="logo" style="left:11px;top:26px"></div>
  <div class="ttl" style="left:45px;top:28px;font-size:15px">Your Awesome Title</div>
  <div class="lbl" style="left:105px;top:50px;font-size:5px">Awesome Subtitle</div>
</section>

<section class="slide four-things" style="left:279px;top:13px">
  <div style="left:70px;top:14px;width:.5px;height:120px;background:#ccc"></div>
  <div style="left:20px;top:73px;width:102px;height:.5px;background:#ccc"></div>
  <div class="icon-c" style="left:31px;top:15px"><svg color="#fff"><use href="#i-target"/></svg></div>
  <div class="icon-c" style="left:88px;top:15px"><svg color="#fff"><use href="#i-hourglass"/></svg></div>
  <div class="icon-c" style="left:31px;top:115px"><svg color="#fff"><use href="#i-bulb"/></svg></div>
  <div class="icon-c" style="left:88px;top:115px"><svg color="#fff"><use href="#i-eye"/></svg></div>
  <p class="tiny" style="left:26px;top:42px;width:38px">Brief note on this idea.</p>
  <p class="tiny" style="left:83px;top:42px;width:38px">Brief note on this idea.</p>
  <p class="tiny" style="left:26px;top:88px;width:38px">Brief note on this idea.</p>
  <p class="tiny" style="left:83px;top:88px;width:38px">Brief note on this idea.</p>
  <svg class="swoosh" viewBox="0 0 262 148" preserveAspectRatio="none">
    <path d="M145 0H262V148H175Q200 80 145 0Z" fill="var(--magenta)"/>
    <path d="M145 0Q200 80 175 148H165Q190 80 135 0Z" fill="var(--orange)"/>
    <path d="M135 0Q185 60 160 148H155Q178 60 128 0Z" fill="var(--grey)"/>
  </svg>
  <div class="ttl ttl-w" style="left:176px;top:9px;font-size:10px">4 Things</div>
  <p class="tiny w" style="left:175px;top:28px;width:80px;color:#fff">This block holds a short summary of the first key idea for the audience.</p>
  <p class="tiny w" style="left:175px;top:80px;width:80px;color:#fff">This block holds a short summary of the second key idea for the audience.</p>
</section>

<section class="slide what-we-do" style="left:552px;top:13px">
  <div class="photo" style="left:0;top:60px;width:261px;height:88px;background:var(--ph-interior)" role="img" aria-label="Photo of a woman in sunglasses seated in a bright interior"></div>
  <svg class="swoosh" viewBox="0 0 262 148" preserveAspectRatio="none">
    <path d="M0 0H262V78Q120 50 0 70Z" fill="#fff"/>
    <path d="M0 70Q120 50 262 78V84Q120 58 0 76Z" fill="var(--grey)"/>
    <path d="M0 76Q120 58 262 84V90Q120 66 0 82Z" fill="var(--orange)"/>
  </svg>
  <div class="logo" style="left:32px;top:12px"></div>
  <div class="ttl" style="left:84px;top:8px;font-size:13px">What We Do?</div>
  <p class="tiny" style="left:33px;top:32px;width:220px">A short overview of the services we offer to teams and the public in workshops and sessions.</p>
</section>

<!-- Row 2 -->
<section class="slide strategy-a" style="left:5px;top:180px">
  <div class="photo" style="left:0;top:0;width:115px;height:148px;background:var(--ph-warm)" role="img" aria-label="Photo of a woman sitting on rocks at sunset"></div>
  <svg class="swoosh" viewBox="0 0 262 148" preserveAspectRatio="none">
    <path d="M115 0Q95 74 115 148V148H110Q88 74 110 0Z" fill="var(--orange)"/>
  </svg>
  <div class="badge" style="left:87px;top:13px">A</div>
  <div class="badge" style="left:84px;top:46px">B</div>
  <div class="badge" style="left:90px;top:75px">C</div>
  <div class="badge" style="left:98px;top:107px">D</div>
  <div class="ttl ttl-w" style="left:7px;top:93px;font-size:10px;line-height:1.3">Our<br>Strategy</div>
  <p class="tiny" style="left:125px;top:15px;width:95px">Short note about this step goes here.</p>
  <p class="tiny" style="left:125px;top:47px;width:95px">Short note about this step goes here.</p>
  <p class="tiny" style="left:125px;top:77px;width:95px">Short note about this step goes here.</p>
  <p class="tiny" style="left:125px;top:109px;width:95px">Short note about this step goes here.</p>
</section>

<section class="slide title-photo" style="left:279px;top:180px">
  <div class="photo" style="left:0;top:0;width:261px;height:148px;background:var(--ph-lake)" role="img" aria-label="Photo of a woman sitting by a lake at dusk"></div>
  <svg class="swoosh" viewBox="0 0 262 148" preserveAspectRatio="none">
    <path d="M0 110Q140 160 262 120V148H0Z" fill="var(--orange)"/>
    <path d="M0 118Q140 168 262 128V148H0Z" fill="#fff"/>
    <path d="M0 122Q140 172 262 134V148H0Z" fill="var(--grey)"/>
  </svg>
  <div class="ttl ttl-w" style="left:42px;top:55px;font-size:15px">Your Awesome Title</div>
  <div class="lbl w" style="left:107px;top:77px;font-size:5px;color:#fff">Awesome Subtitle</div>
</section>

<section class="slide about-me-a" style="left:552px;top:180px">
  <div class="photo" style="left:120px;top:0;width:141px;height:148px;background:var(--ph-meadow)" role="img" aria-label="Photo of a woman in a dress walking through a sunlit meadow"></div>
  <svg class="swoosh" viewBox="0 0 262 148" preserveAspectRatio="none">
    <path d="M120 0Q170 74 140 148H0V0Z" fill="#fff"/>
    <path d="M140 0Q195 74 150 148H140Q170 74 120 0Z" fill="var(--orange)"/>
  </svg>
  <div class="logo" style="left:6px;top:32px"></div>
  <div class="ttl" style="left:24px;top:34px;font-size:11px">About Me</div>
  <p class="tiny" style="left:24px;top:56px;width:95px">Write a few lines about your background, your training style and the groups you work with.</p>
</section>

<!-- Row 3 -->
<section class="slide about-me-b" style="left:5px;top:340px">
  <div class="icon-c" style="left:30px;top:14px;width:20px;height:20px"><svg color="#fff"><use href="#i-award"/></svg></div>
  <div class="lbl" style="left:23px;top:38px">Ipsum Loren</div>
  <div class="icon-c" style="left:30px;top:60px;width:20px;height:20px"><svg color="#fff"><use href="#i-award"/></svg></div>
  <div class="lbl" style="left:23px;top:85px">Ipsum Loren</div>
  <div class="icon-c" style="left:30px;top:104px;width:20px;height:20px"><svg color="#fff"><use href="#i-award"/></svg></div>
  <div class="lbl" style="left:23px;top:128px">Ipsum Loren</div>
  <div style="left:85px;top:0;width:93px;height:148px;background:var(--orange)"></div>
  <div class="photo" style="left:178px;top:0;width:83px;height:148px;background:var(--ph-sunset)" role="img" aria-label="Photo of a person jumping against a sunset sky"></div>
  <div class="ttl ttl-w" style="left:105px;top:13px;font-size:13px;line-height:1.1;text-align:center">About<br>Me</div>
  <p style="left:90px;top:52px;width:84px;font-size:3.6px;line-height:1.3;color:#fff">Lorem Ipsum is simply dummy text of the printing and typesetting industry. Lorem Ipsum has been the industry's standard dummy text ever since the 1500s, when an unknown printer took a galley of type and scrambled it to make a type specimen book. It has survived not only five centuries, but also the leap into electronic typesetting, remaining essentially unchanged.</p>
</section>

<section class="slide checklist" style="left:279px;top:340px">
  <div class="photo" style="left:0;top:0;width:115px;height:148px;background:var(--ph-interior)" role="img" aria-label="Photo of a woman in sunglasses reading at a table"></div>
  <svg class="swoosh" viewBox="0 0 262 148" preserveAspectRatio="none">
    <path d="M115 0Q90 74 115 148H262V0Z" fill="#fff"/>
    <path d="M115 0Q90 74 115 148H108Q84 74 108 0Z" fill="var(--grey)"/>
  </svg>
  <div style="left:121px;top:15px;width:12px;height:12px;border-radius:50%;background:var(--yellow);color:#fff;display:flex;align-items:center;justify-content:center"><svg width="8" height="8"><use href="#i-check"/></svg></div>
  <div style="left:121px;top:47px;width:12px;height:12px;border-radius:50%;border:.6px solid #ccc;color:#ccc;display:flex;align-items:center;justify-content:center"><svg width="8" height="8"><use href="#i-check"/></svg></div>
  <div style="left:121px;top:80px;width:12px;height:12px;border-radius:50%;border:.6px solid #ccc;color:#ccc;display:flex;align-items:center;justify-content:center"><svg width="8" height="8"><use href="#i-check"/></svg></div>
  <div style="left:121px;top:112px;width:12px;height:12px;border-radius:50%;border:.6px solid #ccc;color:#ccc;display:flex;align-items:center;justify-content:center"><svg width="8" height="8"><use href="#i-check"/></svg></div>
  <p class="tiny" style="left:143px;top:15px;width:95px">Short note on this item.</p>
  <p class="tiny" style="left:143px;top:48px;width:95px">Short note on this item.</p>
  <p class="tiny" style="left:143px;top:81px;width:95px">Short note on this item.</p>
  <p class="tiny" style="left:143px;top:113px;width:95px">Short note on this item.</p>
</section>

<section class="slide three-steps" style="left:552px;top:340px">
  <div class="ttl" style="left:108px;top:10px;font-size:10px">3 Steps</div>
  <div class="lbl" style="left:54px;top:37px">Lorem Ipsum</div>
  <div class="lbl" style="left:118px;top:37px">Lorem Ipsum</div>
  <div class="lbl" style="left:180px;top:37px">Lorem Ipsum</div>
  <div style="left:0;top:34px;width:261px;height:.5px;background:#ddd"></div>
  <svg style="left:40px;top:44px;width:215px;height:75px" viewBox="0 0 215 75">
    <path d="M0 0H62L80 37 62 75H0L12 37Z" fill="var(--magenta)"/>
    <path d="M66 0H128L146 37 128 75H66L84 37Z" fill="var(--teal)"/>
    <path d="M132 0H194L212 37 194 75H132L150 37Z" fill="var(--black)"/>
  </svg>
  <svg style="left:78px;top:58px;width:18px;height:18px;color:#fff"><use href="#i-thumb"/></svg>
  <svg style="left:143px;top:58px;width:18px;height:18px;color:#fff"><use href="#i-target"/></svg>
  <svg style="left:208px;top:58px;width:18px;height:18px;color:#fff"><use href="#i-puzzle"/></svg>
  <div class="lbl w" style="left:67px;top:101px;color:#fff">Lorem Ipsum</div>
  <div class="lbl w" style="left:133px;top:101px;color:#fff">Lorem Ipsum</div>
  <div class="lbl w" style="left:198px;top:101px;color:#fff">Lorem Ipsum</div>
</section>

<!-- Row 4 -->
<section class="slide about-training" style="left:5px;top:503px">
  <div class="photo" style="left:160px;top:0;width:101px;height:148px;background:var(--ph-flowers)" role="img" aria-label="Photo of a woman holding flowers over her eyes"></div>
  <svg class="swoosh" viewBox="0 0 262 148" preserveAspectRatio="none">
    <path d="M140 0Q185 74 150 148H0V0Z" fill="#fff"/>
    <path d="M145 0Q190 74 158 148H150Q180 74 135 0Z" fill="var(--orange)"/>
    <path d="M155 0Q198 74 166 148H160Q190 74 148 0Z" fill="var(--grey)"/>
  </svg>
  <div class="logo" style="left:12px;top:16px"></div>
  <div class="ttl" style="left:30px;top:12px;font-size:11px;line-height:1.1">About<br>Training</div>
  <p class="tiny" style="left:30px;top:47px;width:75px">It is a long established fact that a reader will be distracted by the readable content of a page when looking at its layout. The point of using Lorem Ipsum is that it has a more-or-less normal distribution of letters, as opposed to using content here, making it look like readable English. Many desktop publishing packages and web page editors now use Lorem Ipsum as their default model text.</p>
</section>

<section class="slide psychologies" style="left:279px;top:503px">
  <div class="ttl" style="left:85px;top:8px;font-size:10px">Psychologies</div>
  <div style="left:30px;top:28px;width:80px;height:98px;border-radius:40px 40px 30px 30px;background:linear-gradient(180deg,#2a2a2a 0 30%,var(--magenta) 30% 55%,var(--teal) 55% 75%,var(--yellow) 75%)" role="img" aria-label="Illustration of a head silhouette divided into coloured bands"></div>
  <div class="lbl w" style="left:55px;top:64px;color:#fff">Lorem Ipsum</div>
  <div class="lbl w" style="left:55px;top:80px;color:#fff">Lorem Ipsum</div>
  <div class="lbl w" style="left:55px;top:98px;color:#fff">Lorem Ipsum</div>
  <div class="bar" style="left:140px;top:26px;width:115px;height:20px;background:var(--magenta);padding-left:14px"><b>LOREM IPSUM</b><span>Lorem Ipsum is simply dummy text of the printing and typesetting industry.</span></div>
  <div class="num" style="left:132px;top:27px;width:17px;height:17px;background:var(--magenta);border:1.5px solid #fff">A</div>
  <div class="bar" style="left:140px;top:68px;width:115px;height:20px;background:var(--teal);padding-left:14px"><b>LOREM IPSUM</b><span>Lorem Ipsum is simply dummy text of the printing and typesetting industry.</span></div>
  <div class="num" style="left:132px;top:69px;width:17px;height:17px;background:var(--teal);border:1.5px solid #fff">B</div>
  <div class="bar" style="left:140px;top:112px;width:115px;height:20px;background:var(--yellow);padding-left:14px"><b>LOREM IPSUM</b><span>Lorem Ipsum is simply dummy text of the printing and typesetting industry.</span></div>
  <div class="num" style="left:132px;top:113px;width:17px;height:17px;background:var(--yellow);border:1.5px solid #fff">C</div>
</section>

<section class="slide strategy-b" style="left:552px;top:503px">
  <div class="photo" style="left:0;top:0;width:261px;height:148px;background:var(--ph-warm)" role="img" aria-label="Photo of a woman sitting on rocks at sunset"></div>
  <div style="left:100px;top:0;width:161px;height:148px;background:rgba(255,255,255,.92)"></div>
  <svg class="swoosh" viewBox="0 0 262 148" preserveAspectRatio="none">
    <path d="M100 0Q80 74 100 148H95Q74 74 95 0Z" fill="var(--orange)"/>
  </svg>
  <div class="badge" style="left:86px;top:12px">A</div>
  <div class="badge" style="left:84px;top:44px">B</div>
  <div class="badge" style="left:90px;top:76px">C</div>
  <div class="badge" style="left:98px;top:108px">D</div>
  <div class="ttl ttl-w" style="left:7px;top:95px;font-size:10px;line-height:1.2">Our<br>Strategy</div>
  <div class="bar" style="left:118px;top:12px;width:110px;height:14px;background:var(--magenta)"><span>Short note about this step goes here.</span></div>
  <div class="bar" style="left:118px;top:44px;width:110px;height:14px;background:var(--magenta)"><span>Short note about this step goes here.</span></div>
  <div class="bar" style="left:118px;top:76px;width:110px;height:14px;background:var(--magenta)"><span>Short note about this step goes here.</span></div>
  <div class="bar" style="left:118px;top:108px;width:110px;height:14px;background:var(--magenta)"><span>Short note about this step goes here.</span></div>
</section>

<!-- Row 5 -->
<section class="slide coaching-a" style="left:5px;top:680px">
  <div class="photo" style="left:120px;top:0;width:141px;height:148px;background:var(--ph-meadow)" role="img" aria-label="Photo of a woman in a dress walking through a sunlit meadow"></div>
  <svg class="swoosh" viewBox="0 0 262 148" preserveAspectRatio="none">
    <path d="M0 0H150Q130 60 95 148H0Z" fill="#fff"/>
    <path d="M150 0Q130 60 95 148H105Q140 60 162 0Z" fill="var(--orange)"/>
    <path d="M170 0Q150 50 125 148H130Q155 50 178 0Z" fill="var(--yellow)"/>
  </svg>
  <div class="ttl" style="left:16px;top:10px;font-size:13px;line-height:1.1;text-align:center">About<br>Coaching</div>
  <div class="lbl" style="left:18px;top:57px;text-transform:none;font-size:5px;color:var(--teal)">Lorem Ipsum</div>
  <div class="lbl" style="left:18px;top:85px;text-transform:none;font-size:5px;color:var(--teal)">Lorem Ipsum</div>
  <div class="lbl" style="left:18px;top:112px;text-transform:none;font-size:5px;color:var(--teal)">Lorem Ipsum</div>
  <div class="bar" style="left:96px;top:52px;width:145px;height:17px;background:var(--magenta)"><span style="font-size:4px">Lorem Ipsum is simply dummy text of the printing and typesetting industry. Lorem Ipsum has been the industry's standard dummy text ever since the 1500s</span></div>
  <div class="bar" style="left:96px;top:80px;width:145px;height:17px;background:var(--magenta)"><span style="font-size:4px">Lorem Ipsum is simply dummy text of the printing and typesetting industry. Lorem Ipsum has been the industry's standard dummy text ever since the 1500s</span></div>
  <div class="bar" style="left:96px;top:107px;width:145px;height:17px;background:var(--magenta)"><span style="font-size:4px">Lorem Ipsum is simply dummy text of the printing and typesetting industry. Lorem Ipsum has been the industry's standard dummy text ever since the 1500s</span></div>
</section>

<section class="slide coaching-b" style="left:279px;top:680px">
  <div class="photo" style="left:150px;top:0;width:111px;height:148px;background:var(--ph-meadow)" role="img" aria-label="Photo of a woman in a dress walking through a sunlit meadow"></div>
  <svg class="swoosh" viewBox="0 0 262 148" preserveAspectRatio="none">
    <path d="M0 0H170Q150 60 150 148H0Z" fill="#fff"/>
    <path d="M170 0Q150 60 150 148H158Q160 60 180 0Z" fill="var(--orange)"/>
  </svg>
  <div class="logo" style="left:14px;top:14px"></div>
  <div class="ttl" style="left:34px;top:8px;font-size:10px;line-height:1.15">About<br>Coaching</div>
  <div style="left:10px;top:44px;width:152px;height:38px;background:var(--magenta);color:#fff;text-align:center;padding:3px 5px">
    <div style="font-size:3.4px;margin-bottom:2px">YOUR AWESOME TEXT</div>
    <div style="font-size:3.4px;line-height:1.35">Lorem Ipsum is simply dummy text of the printing and typesetting industry. Lorem Ipsum has been the industry's standard dummy text ever since the 1500s, when an unknown printer took a galley of type and scrambled it to make a type specimen book.</div>
  </div>
  <div class="icon-c" style="left:18px;top:95px;width:18px;height:18px"><svg color="#fff"><use href="#i-smile"/></svg></div>
  <div class="icon-c" style="left:68px;top:95px;width:18px;height:18px"><svg color="#fff"><use href="#i-target"/></svg></div>
  <div class="icon-c" style="left:118px;top:95px;width:18px;height:18px"><svg color="#fff"><use href="#i-eye"/></svg></div>
  <div class="lbl" style="left:12px;top:119px">Lorem Ipsum</div>
  <div class="lbl" style="left:62px;top:119px">Lorem Ipsum</div>
  <div class="lbl" style="left:112px;top:119px">Lorem Ipsum</div>
</section>

<section class="slide gallery-a" style="left:552px;top:680px">
  <svg class="swoosh" viewBox="0 0 262 148" preserveAspectRatio="none">
    <path d="M130 60Q200 20 262 40V80Q200 60 140 90Z" fill="#e2e2e2"/>
  </svg>
  <div class="lbl" style="left:26px;top:5px">Lorem Ipsum</div>
  <div class="lbl" style="left:24px;top:13px;font-size:3px;color:#888">Some short text here</div>
  <div class="photo" style="left:14px;top:35px;width:70px;height:113px;background:var(--ph-sunset)" role="img" aria-label="Photo of a person with arms outstretched at sunset"></div>
  <div class="photo" style="left:98px;top:2px;width:70px;height:105px;background:var(--ph-warm)" role="img" aria-label="Photo of a woman in a meadow with sunlight behind her"></div>
  <div class="lbl" style="left:110px;top:116px">Lorem Ipsum</div>
  <div class="lbl" style="left:107px;top:124px;font-size:3px;color:#888">Some short text here</div>
  <div class="ttl" style="left:178px;top:69px;font-size:12px;line-height:1.15;text-align:right">Our<br>Gallery</div>
</section>

<!-- Row 6 -->
<section class="slide strategy-c" style="left:5px;top:847px">
  <div class="ttl" style="left:85px;top:8px;font-size:10px">Our Strategy</div>
  <svg style="left:38px;top:42px;width:190px;height:64px" viewBox="0 0 190 64" fill="none" stroke="var(--orange)" stroke-width="5">
    <path d="M20 24a18 18 0 1 1 34 8a18 18 0 1 0 34 0a18 18 0 1 1 34 0a18 18 0 1 0 34 0a18 18 0 1 1 34 8" stroke-linecap="round"/>
  </svg>
  <div class="num" style="left:64px;top:55px;width:17px;height:17px;background:var(--orange)">1</div>
  <div class="num" style="left:89px;top:80px;width:17px;height:17px;background:var(--orange)">2</div>
  <div class="num" style="left:115px;top:55px;width:17px;height:17px;background:var(--black)">3</div>
  <div class="num" style="left:141px;top:80px;width:17px;height:17px;background:var(--magenta)">4</div>
  <div class="num" style="left:167px;top:55px;width:17px;height:17px;background:var(--teal)">5</div>
  <div class="num" style="left:192px;top:80px;width:17px;height:17px;background:var(--black)">6</div>
  <div class="lbl" style="left:105px;top:26px">Lorem Ipsum</div><p class="tiny" style="left:100px;top:31px;width:32px;text-align:center">Short note on this step.</p>
  <div class="lbl" style="left:158px;top:26px">Lorem Ipsum</div><p class="tiny" style="left:153px;top:31px;width:32px;text-align:center">Short note on this step.</p>
  <div class="lbl" style="left:28px;top:72px;color:var(--magenta)">Lorem Ipsum</div><p class="tiny" style="left:14px;top:77px;width:40px;color:var(--magenta);text-align:right">Short note on this step.</p>
  <div class="lbl" style="left:82px;top:110px">Lorem Ipsum</div><p class="tiny" style="left:77px;top:115px;width:32px;text-align:center">Short note on this step.</p>
  <div class="lbl" style="left:134px;top:110px;color:var(--magenta)">Lorem Ipsum</div><p class="tiny" style="left:129px;top:115px;width:32px;text-align:center;color:var(--magenta)">Short note on this step.</p>
  <div class="lbl" style="left:212px;top:65px">Lorem Ipsum</div><p class="tiny" style="left:212px;top:70px;width:38px">Short note on this step.</p>
</section>

<section class="slide messages" style="left:279px;top:847px">
  <div class="ttl" style="left:88px;top:22px;font-size:10px">Our Messages</div>
  <div class="lbl" style="left:28px;top:42px">Lorem Ipsum</div>
  <div class="lbl" style="left:112px;top:42px">Lorem Ipsum</div>
  <div class="lbl" style="left:198px;top:42px">Lorem Ipsum</div>
  <p class="tiny" style="left:8px;top:49px;width:72px;text-align:center">Lorem Ipsum is simply dummy text of the printing and typesetting industry. Lorem Ipsum has been the industry's standard dummy text ever since the 1500s.</p>
  <p class="tiny" style="left:94px;top:49px;width:72px;text-align:center">Lorem Ipsum is simply dummy text of the printing and typesetting industry. Lorem Ipsum has been the industry's standard dummy text ever since the 1500s.</p>
  <p class="tiny" style="left:180px;top:49px;width:72px;text-align:center">Lorem Ipsum is simply dummy text of the printing and typesetting industry. Lorem Ipsum has been the industry's standard dummy text ever since the 1500s.</p>
  <div style="left:0;top:88px;width:87px;height:60px;background:var(--magenta)"></div>
  <div style="left:87px;top:88px;width:87px;height:60px;background:var(--teal)"></div>
  <div style="left:174px;top:88px;width:87px;height:60px;background:var(--black)"></div>
  <svg style="left:33px;top:105px;width:20px;height:20px;color:#fff"><use href="#i-thumb"/></svg>
  <svg style="left:120px;top:105px;width:20px;height:20px;color:#fff"><use href="#i-target"/></svg>
  <svg style="left:207px;top:105px;width:20px;height:20px;color:#fff"><use href="#i-puzzle"/></svg>
  <div class="lbl w" style="left:24px;top:134px;color:#fff">Lorem Ipsum</div>
  <div class="lbl w" style="left:111px;top:134px;color:#fff">Lorem Ipsum</div>
  <div class="lbl w" style="left:198px;top:134px;color:#fff">Lorem Ipsum</div>
</section>

<section class="slide gallery-b" style="left:552px;top:847px">
  <svg class="swoosh" viewBox="0 0 262 148" preserveAspectRatio="none">
    <path d="M0 130Q130 80 262 110V120Q130 92 0 140Z" fill="#e2e2e2"/>
  </svg>
  <div class="lbl" style="left:31px;top:5px;font-size:4.4px">Gallery 1</div>
  <div class="lbl" style="left:24px;top:13px;font-size:3px;color:#888">Some short text here</div>
  <div class="photo" style="left:6px;top:36px;width:75px;height:112px;background:var(--ph-interior)" role="img" aria-label="Photo of a woman in sunglasses in a bright room"></div>
  <div class="photo" style="left:96px;top:2px;width:72px;height:105px;background:var(--ph-meadow)" role="img" aria-label="Photo of a woman walking through a meadow"></div>
  <div class="lbl" style="left:117px;top:118px;font-size:4.4px">Gallery 2</div>
  <div class="lbl" style="left:109px;top:126px;font-size:3px;color:#888">Some short text here</div>
  <div class="lbl" style="left:203px;top:5px;font-size:4.4px">Gallery 3</div>
  <div class="lbl" style="left:193px;top:13px;font-size:3px;color:#888">Some short text here</div>
  <div class="photo" style="left:178px;top:36px;width:83px;height:112px;background:var(--ph-warm)" role="img" aria-label="Photo of a woman sitting on rocks at sunset"></div>
</section>

<!-- Row 7 -->
<section class="slide pyramid" style="left:5px;top:1038px">
  <svg style="left:10px;top:8px;width:100px;height:132px" viewBox="0 0 100 132">
    <path d="M50 0L68 40H32Z" fill="var(--magenta)"/>
    <path d="M30 45H70L88 85H12Z" fill="var(--teal)"/>
    <path d="M10 90H90L100 132H0Z" fill="var(--black)"/>
  </svg>
  <svg style="left:52px;top:26px;width:16px;height:16px;color:#fff"><use href="#i-thumb"/></svg>
  <svg style="left:51px;top:63px;width:18px;height:18px;color:#fff"><use href="#i-target"/></svg>
  <svg style="left:50px;top:106px;width:20px;height:20px;color:#fff"><use href="#i-puzzle"/></svg>
  <div class="bar" style="left:124px;top:26px;width:117px;height:18px;background:var(--magenta);padding-left:12px"><b>LOREM IPSUM</b><span>Lorem Ipsum is simply dummy text of the printing and typesetting industry.</span></div>
  <div class="num" style="left:113px;top:26px;width:17px;height:17px;background:var(--magenta);border:1.5px solid #fff">1</div>
  <div class="bar" style="left:124px;top:67px;width:117px;height:18px;background:var(--teal);padding-left:12px"><b>LOREM IPSUM</b><span>Lorem Ipsum is simply dummy text of the printing and typesetting industry.</span></div>
  <div class="num" style="left:113px;top:67px;width:17px;height:17px;background:var(--teal);border:1.5px solid #fff">2</div>
  <div class="bar" style="left:124px;top:106px;width:117px;height:18px;background:var(--yellow);padding-left:12px"><b>LOREM IPSUM</b><span>Lorem Ipsum is simply dummy text of the printing and typesetting industry.</span></div>
  <div class="num" style="left:113px;top:106px;width:17px;height:17px;background:var(--yellow);border:1.5px solid #fff">3</div>
</section>

<section class="slide coaching-c" style="left:279px;top:1038px">
  <div class="photo" style="left:130px;top:0;width:131px;height:148px;background:var(--ph-meadow)" role="img" aria-label="Photo of a woman in a dress walking through a sunlit meadow"></div>
  <svg class="swoosh" viewBox="0 0 262 148" preserveAspectRatio="none">
    <path d="M0 0H165Q140 70 160 148H0Z" fill="#fff"/>
    <path d="M165 0Q140 70 160 148H168Q150 70 175 0Z" fill="var(--orange)"/>
    <path d="M180 0Q160 70 175 148H180Q166 70 186 0Z" fill="var(--yellow)"/>
  </svg>
  <div class="logo" style="left:8px;top:30px"></div>
  <div class="ttl" style="left:27px;top:26px;font-size:10px;line-height:1.15">About<br>Coaching</div>
  <div style="left:22px;top:56px;width:150px;height:40px;background:var(--magenta);color:#fff;padding:4px 5px;z-index:2">
    <div style="font-size:3.4px;margin-bottom:2px">YOUR AWESOME TEXT</div>
    <div style="font-size:3.4px;line-height:1.35">Lorem Ipsum is simply dummy text of the printing and typesetting industry. Lorem Ipsum has been the industry's standard dummy text ever since the 1500s, when an unknown printer took a galley of type and scrambled it to make a type specimen book.</div>
  </div>
  <div class="icon-c" style="left:34px;top:106px;width:18px;height:18px"><svg color="#fff"><use href="#i-smile"/></svg></div>
  <div class="icon-c" style="left:86px;top:106px;width:18px;height:18px"><svg color="#fff"><use href="#i-target"/></svg></div>
  <div class="icon-c" style="left:138px;top:106px;width:18px;height:18px"><svg color="#fff"><use href="#i-eye"/></svg></div>
  <div class="lbl" style="left:28px;top:130px">Lorem Ipsum</div>
  <div class="lbl" style="left:80px;top:130px">Lorem Ipsum</div>
  <div class="lbl" style="left:132px;top:130px">Lorem Ipsum</div>
</section>

<section class="slide icon-ring" style="left:552px;top:1038px">
  <svg style="left:25px;top:12px;width:110px;height:125px" viewBox="0 0 110 125" fill="none" stroke="#ddd" stroke-width="1"><circle cx="55" cy="62" r="45"/></svg>
  <div style="left:76px;top:54px;width:10px;height:30px;border-radius:5px;background:var(--magenta)" role="img" aria-label="Pictogram of a person"></div>
  <div class="num" style="left:73px;top:14px;width:14px;height:14px;background:var(--black)"><svg width="8" height="8"><use href="#i-target"/></svg></div>
  <div class="num" style="left:36px;top:33px;width:14px;height:14px;background:var(--teal)"><svg width="8" height="8"><use href="#i-heart"/></svg></div>
  <div class="num" style="left:110px;top:33px;width:14px;height:14px;background:var(--yellow)"><svg width="8" height="8"><use href="#i-puzzle"/></svg></div>
  <div class="num" style="left:26px;top:68px;width:14px;height:14px;background:var(--magenta)"><svg width="8" height="8"><use href="#i-award"/></svg></div>
  <div class="num" style="left:120px;top:68px;width:14px;height:14px;background:var(--magenta)"><svg width="8" height="8"><use href="#i-pin"/></svg></div>
  <div class="num" style="left:36px;top:103px;width:14px;height:14px;background:var(--black)"><svg width="8" height="8"><use href="#i-check"/></svg></div>
  <div class="num" style="left:110px;top:103px;width:14px;height:14px;background:var(--teal)"><svg width="8" height="8"><use href="#i-smile"/></svg></div>
  <div class="num" style="left:73px;top:120px;width:14px;height:14px;background:var(--yellow)"><svg width="8" height="8"><use href="#i-dollar"/></svg></div>
  <div class="lbl" style="left:70px;top:31px;font-size:2.8px">Lorem Ipsum</div>
  <div class="lbl" style="left:72px;top:137px;font-size:2.8px">Lorem Ipsum</div>

  <div class="lbl" style="left:146px;top:16px;font-size:2.8px">Lorem</div>
  <div style="left:163px;top:15px;width:80px;height:5px;border-radius:3px;background:#eee"><div style="width:75%;height:100%;border-radius:3px;background:var(--magenta)"></div></div>
  <div class="lbl" style="left:146px;top:31px;font-size:2.8px">Lorem</div>
  <div style="left:163px;top:30px;width:80px;height:5px;border-radius:3px;background:#eee"><div style="width:85%;height:100%;border-radius:3px;background:var(--black)"></div></div>
  <div class="lbl" style="left:146px;top:46px;font-size:2.8px">Lorem</div>
  <div style="left:163px;top:45px;width:80px;height:5px;border-radius:3px;background:#eee"><div style="width:65%;height:100%;border-radius:3px;background:var(--teal)"></div></div>
  <div class="lbl" style="left:146px;top:61px;font-size:2.8px">Lorem</div>
  <div style="left:163px;top:60px;width:80px;height:5px;border-radius:3px;background:#eee"><div style="width:55%;height:100%;border-radius:3px;background:var(--yellow)"></div></div>
  <div class="lbl" style="left:146px;top:76px;font-size:2.8px">Lorem</div>
  <div style="left:163px;top:75px;width:80px;height:5px;border-radius:3px;background:#eee"><div style="width:80%;height:100%;border-radius:3px;background:var(--magenta)"></div></div>
  <div class="lbl" style="left:146px;top:91px;font-size:2.8px">Lorem</div>
  <div style="left:163px;top:90px;width:80px;height:5px;border-radius:3px;background:#eee"><div style="width:60%;height:100%;border-radius:3px;background:var(--teal)"></div></div>
  <div class="lbl" style="left:146px;top:106px;font-size:2.8px">Lorem</div>
  <div style="left:163px;top:105px;width:80px;height:5px;border-radius:3px;background:#eee"><div style="width:90%;height:100%;border-radius:3px;background:var(--black)"></div></div>
  <div class="lbl" style="left:146px;top:121px;font-size:2.8px">Lorem</div>
  <div style="left:163px;top:120px;width:80px;height:5px;border-radius:3px;background:#eee"><div style="width:50%;height:100%;border-radius:3px;background:var(--yellow)"></div></div>
</section>

</main>
</body>
</html>
```